Bright Harbor Theatre Academy Business Card

We need a professional looking card for the Bright Harbor Theatre Academy. The logo is attached.
The owner is: Marla Quintrell
Phone Number: 303-555-0147
Email: bhtheatreacademy@mailbox-example.com
Website: bhtheatre-example.com
Somewhere on the front of the card we would like to see the slogan: Step into the limelight
On the back we would like to see the quote: All the world's a stage. -Edmund Larkwood
We are open to different colors for the wording or maybe just black. Something that will go well with the logo.
Individuals seeking a professional children's theatre.
Business

```html
<!DOCTYPE html>
<html lang="en">
<head>
<meta charset="utf-8">
<title>Bright Harbor Theatre Academy – Business Card</title>
<link rel="stylesheet" href="https://fonts.googleapis.com/css2?family=Open+Sans:wght@400;600;700&family=Montserrat:wght@700&display=swap">
<style>
  :root {
    --curtain-red: #82161a;
    --card-white: #ffffff;
    --backdrop: #ededed;
    --ink: #1c1c1c;
    --text-on-red: #f4ecec;
  }
  * { box-sizing: border-box; margin: 0; padding: 0; }
  html, body {
    width: 1200px; height: 720px; overflow: hidden;
    background: var(--backdrop);
    font-family: "Open Sans", Arial, sans-serif;
  }
  .canvas {
    position: relative; width: 1200px; height: 720px;
    display: flex; align-items: center; justify-content: center; gap: 50px;
  }
  .card {
    position: relative; width: 525px; height: 300px;
    background: var(--card-white);
    box-shadow: 0 2px 6px rgba(0,0,0,0.12);
    overflow: hidden;
  }
  .band { position: absolute; left: 0; right: 0; background: var(--curtain-red); }

  /* Back of card */
  .card-back .band-top { top: 0; height: 36px; }
  .card-back .band-bottom { top: 126px; bottom: 0; }
  .card-back .brand {
    position: absolute; top: 36px; height: 90px; left: 0; right: 0;
    display: flex; align-items: center; justify-content: center; gap: 10px;
  }
  .card-back .quote {
    position: absolute; top: 140px; left: 0; right: 0; text-align: center;
    color: var(--text-on-red); font-size: 15px; font-weight: 400;
  }

  /* Front of card */
  .card-front .band-top { top: 0; height: 40px; }
  .card-front .band-main { top: 120px; height: 150px; }
  .card-front .brand {
    position: absolute; top: 40px; height: 80px; left: 36px;
    display: flex; align-items: center; gap: 8px;
  }
  .brand-mark { width: 14px; height: 14px; background: var(--curtain-red); flex: none; }
  .brand-name { font-size: 17px; font-weight: 600; color: var(--ink); letter-spacing: 0.2px; }
  .card-front .owner {
    position: absolute; top: 50px; right: 22px; text-align: right; color: var(--ink);
  }
  .owner-name { font-family: "Montserrat", Arial, sans-serif; font-weight: 700; font-size: 13px; }
  .owner-role { font-size: 11px; line-height: 1; }
  .card-front .slogan {
    position: absolute; top: 160px; left: 70px;
    color: var(--text-on-red); font-size: 12.5px;
  }
  .card-front .contact {
    position: absolute; top: 152px; right: 22px; text-align: right;
    color: var(--text-on-red); font-size: 12px; line-height: 22px; list-style: none;
  }
  .contact strong { font-weight: 700; }
</style>
</head>
<body>
<main class="canvas">
  <section class="card card-back" aria-label="Card back">
    <div class="band band-top"></div>
    <div class="brand">
      <span class="brand-mark"></span>
      <span class="brand-name">Bright Harbor Theatre Academy</span>
    </div>
    <div class="band band-bottom"></div>
    <p class="quote">All the world's a stage - Edmund Larkwood</p>
  </section>

  <section class="card card-front" aria-label="Card front">
    <div class="band band-top"></div>
    <div class="brand">
      <span class="brand-mark"></span>
      <span class="brand-name">Bright Harbor Theatre Academy</span>
    </div>
    <div class="owner">
      <p class="owner-name">Marla Quintrell</p>
      <p class="owner-role">owner</p>
    </div>
    <div class="band band-main"></div>
    <p class="slogan">Step into the limelight</p>
    <ul class="contact">
      <li>Phone: 303-555-0147</li>
      <li>Email: <strong>bhtheatreacademy</strong>@mailbox-example.com</li>
      <li>Website: <strong>bhtheatre-example</strong>.com</li>
    </ul>
  </section>
</main>
</body>
</html>
```